Business Card for Financial Asset Management Company

Now we are launching a new company based in Tokyo.
The company information is below;

Company Name: Caldera Stewardship

Operations: Financial assets management, Proposing forming portfolio of assets, Consulting service, and advising to enhance your company's financial health

Corporate Colour: Japan Blue or Navy like below
http://pages.art.velmoreu.edu/tkovan/images/Indigo/Aqua-Indigo-104.jpg

It's dark and deep, and will get to fit to our clients as our relationships last longer and longer.

Our images for this colour are "Japanese style" and "pride in our craftmanship" , and also "gentle".

Corporate Key Image: an order taker who is sincere, polite, but courageous

We don't have our logo yet so please feel free to put any symbol on your design.

Please do not hesitate about asking any questions.
Thank you :-)

Reason: We are still discussin on final decision. Thank you for your understanding.

```html
<!DOCTYPE html>
<html lang="en">
<head>
<meta charset="UTF-8">
<title>Caldera Stewardship – Business Card</title>
<link rel="stylesheet" href="https://fonts.googleapis.com/css2?family=Saira+Semi+Condensed:wght@700&family=Open+Sans:wght@400&display=swap">
<style>
  :root {
    --backdrop: #e4e5e8;
    --card-white: #ffffff;
    --indigo: #3a3a9e;
    --indigo-deep: #141446;
    --navy: #1f1f5c;
    --ink: #111118;
    --sphere-light: #f6f5fb;
    --sphere-mid: #d9d6ef;
    --sphere-edge: #a9a4d4;
    --bullet: #e0702a;
    --text-grey: #3b3b4a;
    --paper-text: #ffffff;
  }
  * { margin: 0; padding: 0; box-sizing: border-box; }
  html, body {
    width: 1200px;
    height: 960px;
    overflow: hidden;
    background: var(--backdrop);
  }
  .canvas {
    position: relative;
    width: 1200px;
    height: 960px;
  }
  .card {
    position: absolute;
    top: 330px;
    width: 500px;
    height: 300px;
    overflow: hidden;
    box-shadow: 0 6px 18px rgba(0,0,0,0.18);
  }
  .card-front { left: 60px; background: var(--card-white); }
  .card-back { left: 640px; background: var(--indigo-deep); }
  .card-art {
    position: absolute;
    inset: 0;
    width: 100%;
    height: 100%;
  }
  .company-name {
    position: absolute;
    font-family: "Saira Semi Condensed", "Arial Narrow", sans-serif;
    font-weight: 700;
    text-transform: uppercase;
    letter-spacing: 2px;
    line-height: 1.05;
  }
  .card-front .company-name {
    left: 34px;
    top: 116px;
    font-size: 25px;
    color: var(--navy);
    text-align: right;
  }
  .card-back .company-name {
    left: 0;
    right: 0;
    top: 118px;
    font-size: 28px;
    color: var(--paper-text);
    text-align: center;
    display: flex;
    align-items: center;
    justify-content: center;
    gap: 14px;
  }
  .name-mark {
    width: 22px;
    height: 22px;
    background: var(--paper-text);
    flex: none;
  }
  .services {
    position: absolute;
    left: 250px;
    top: 178px;
    list-style: none;
    font-family: "Open Sans", Arial, sans-serif;
    font-size: 10px;
    line-height: 15px;
    color: var(--text-grey);
  }
  .services li::before {
    content: "";
    display: inline-block;
    width: 5px;
    height: 5px;
    margin-right: 5px;
    background: var(--bullet);
    border-radius: 50%;
    vertical-align: middle;
  }
</style>
</head>
<body>
<main class="canvas">

  <section class="card card-front" aria-label="Business card front">
    <svg class="card-art" viewBox="0 0 500 300" aria-hidden="true">
      <defs>
        <radialGradient id="sphere-fill" cx="0.45" cy="0.45" r="0.6">
          <stop offset="0" stop-color="var(--sphere-light)"/>
          <stop offset="0.6" stop-color="var(--sphere-mid)"/>
          <stop offset="1" stop-color="var(--sphere-edge)"/>
        </radialGradient>
      </defs>
      <circle cx="430" cy="60" r="110" fill="none" stroke="var(--indigo)" stroke-width="18"/>
      <circle cx="365" cy="125" r="140" fill="url(#sphere-fill)"/>
      <rect x="0" y="256" width="225" height="10" fill="var(--indigo)"/>
      <rect x="215" y="256" width="10" height="44" fill="var(--indigo)"/>
      <rect x="0" y="266" width="205" height="34" fill="var(--ink)"/>
    </svg>
    <h1 class="company-name">Caldera<br>Stewardship</h1>
    <ul class="services">
      <li>Financial Assets Management</li>
      <li>Proposing forming portfolio of Assets</li>
      <li>Consulting service</li>
      <li>Advising to enhance your company's financial health</li>
    </ul>
  </section>

  <section class="card card-back" aria-label="Business card back">
    <svg class="card-art" viewBox="0 0 500 300" aria-hidden="true">
      <defs>
        <linearGradient id="back-fill" x1="0" y1="0" x2="1" y2="1">
          <stop offset="0" stop-color="#2b2b86"/>
          <stop offset="0.55" stop-color="#1b1b5e"/>
          <stop offset="1" stop-color="#0c0c30"/>
        </linearGradient>
        <linearGradient id="sweep" x1="0" y1="0" x2="1" y2="0">
          <stop offset="0" stop-color="#4a4ab8" stop-opacity="0"/>
          <stop offset="0.5" stop-color="#4a4ab8" stop-opacity="0.8"/>
          <stop offset="1" stop-color="#4a4ab8" stop-opacity="0.2"/>
        </linearGradient>
      </defs>
      <rect width="500" height="300" fill="url(#back-fill)"/>
      <path d="M0 70 C120 20 300 30 500 90 L500 110 C300 55 140 50 0 95 Z" fill="url(#sweep)" opacity="0.6"/>
      <path d="M60 240 C180 200 330 200 470 225 L460 240 C330 222 200 225 70 255 Z" fill="url(#sweep)"/>
    </svg>
    <h2 class="company-name"><span class="name-mark"></span>Caldera Stewardship</h2>
  </section>

</main>
</body>
</html>
```